Tumble Nest - mobile play centre poster designs

Who are we - we are a mobile playground business that specialises in providing entertainment to children in a safe, clean environment either at home or in a function centre. Brief - create 4 different signs to be displayed on our playgrounds. Please find attached 3 photos from our competitors to use as a guide. Corflute sign - size A1 Toddler zone - size A1 Playground rules - size A4 No climbing - size 20cmx8cm sending through photos and documents now.
Colors
Designer to choose colors to be used in the design.
Requirements
Must have
- Colour, be very specific with the rules, pictures

```html
<!DOCTYPE html>
<html lang="en">
<head>
<meta charset="utf-8">
<title>Tumble Nest – Playground Signage</title>
<link href="https://fonts.googleapis.com/css2?family=Titan+One&family=Rubik:wght@500;700&family=Inter:wght@300;500;600;800&display=swap" rel="stylesheet">
<style>
  :root{
    --board:#1e1e20;
    --white:#ffffff;
    --ink:#1a1a1a;
    --grey:#5a5a5a;
    --red:#e41e26;
    --orange:#f7891f;
    --amber:#fbb117;
    --yellow:#ffc710;
    --lime:#8dc63f;
    --green:#9aca3c;
    --purple:#8e2a8f;
    --blue:#1b75bc;
    --sky:#5ad4fb;
  }
  *{box-sizing:border-box;margin:0;padding:0}
  html,body{width:1200px;height:1126px;overflow:hidden;background:var(--board)}
  .sheet{position:relative;width:1200px;height:1126px;background:var(--board);font-family:"Inter",Arial,sans-serif;color:var(--ink)}

  .poster{position:absolute;top:39px;width:341px;height:484px;overflow:hidden}
  .poster .card{position:absolute;left:19px;top:22px;width:303px;height:441px;background:var(--white);border-radius:18px}
  .poster-rules{left:50px;background:
      radial-gradient(circle at 92% 4%,#ff9d6c 0 22%,transparent 23%),
      radial-gradient(circle at 10% 40%,#ff7f6e 0 18%,transparent 19%),
      radial-gradient(circle at 80% 96%,#ff936b 0 20%,transparent 21%),
      linear-gradient(160deg,#fd6b80,#fc5a7b 60%,#ff8a6d)}
  .poster-toddler{left:429px;background:
      radial-gradient(circle at 62% 0%,#f776f0 0 16%,transparent 17%),
      radial-gradient(circle at 55% 100%,#f57af0 0 14%,transparent 15%),
      radial-gradient(circle at 4% 80%,#9b4ff6 0 20%,transparent 21%),
      linear-gradient(160deg,#6a3df5,#7f48f6 55%,#a656f7)}
  .poster-climb{left:807px;background:
      radial-gradient(circle at 60% 0%,#f9d56e 0 18%,transparent 19%),
      radial-gradient(circle at 95% 90%,#f9cf6c 0 20%,transparent 21%),
      radial-gradient(circle at 0% 50%,#fbc463 0 16%,transparent 17%),
      linear-gradient(160deg,#fba45a,#fcb25f 60%,#f9c268)}
  .pin{position:absolute;width:5px;height:5px;border-radius:50%;background:var(--white)}

  .brand{position:absolute;display:flex;flex-direction:column;font-family:"Rubik",Arial,sans-serif}
  .brand-name{display:flex;align-items:center;gap:5px;font-weight:700;color:var(--purple);line-height:1}
  .brand-name i{display:inline-block;border-radius:50%;background:var(--orange)}
  .brand-tag{font-weight:500;color:var(--grey);letter-spacing:.06em;margin-top:3px}
  .brand-sm .brand-name{font-size:22px}
  .brand-sm .brand-name i{width:14px;height:14px}
  .brand-sm .brand-tag{font-size:9px}

  /* Playground rules */
  .age{position:absolute;left:34px;top:95px;font-family:"Rubik",Arial,sans-serif;font-weight:700;font-size:18px}
  .supervise{position:absolute;left:34px;top:119px;width:270px;font-size:11.6px;line-height:17px;font-weight:600;color:var(--orange)}
  .supervise b{color:var(--ink);font-family:"Rubik",Arial,sans-serif;font-weight:700}
  .rules-band{position:absolute;left:0;top:161px;width:312px;height:44px;background:var(--blue);border-radius:0 22px 22px 0;display:flex;align-items:center;padding-left:36px;font-family:"Titan One",sans-serif;color:var(--yellow);font-size:22px;letter-spacing:.02em}
  .rules-band small{font-size:14px;margin-left:8px;margin-top:4px}
  .rule{position:absolute;display:flex;align-items:center;gap:7px;width:140px}
  .rule svg{flex:none;width:47px;height:47px}
  .rule-no{font-weight:800;color:var(--amber);font-size:17px;line-height:1}
  .rule-label{font-weight:600;font-size:10.4px;line-height:13px;margin-top:2px}
  .rule-label small{display:block;font-size:7.5px;line-height:10px;font-weight:500}

  /* Toddler zone */
  .zone-band{position:absolute;left:0;top:102px;width:243px;height:44px;background:var(--yellow);border-radius:0 22px 22px 0;display:flex;align-items:center;padding-left:35px;font-family:"Titan One",sans-serif;color:var(--purple);font-size:22px;letter-spacing:.02em}
  .zone-age{position:absolute;left:36px;top:155px;font-family:"Rubik",Arial,sans-serif;font-weight:700;font-size:18px;color:var(--purple)}
  .zone-notes{position:absolute;left:36px;top:177px;font-size:12px;font-weight:600;line-height:17.5px}
  .zone-notes em{font-style:normal;color:var(--lime)}
  .zone-box{position:absolute;left:88px;top:222px;width:213px;height:225px;border:2.5px solid var(--yellow);border-radius:15px;padding:16px 18px 0 20px;font-size:11.4px;line-height:17.1px;font-weight:600;text-align:justify;text-align-last:justify}
  .zone-box em{font-style:normal;color:var(--lime)}

  /* No climbing A4 */
  .poster-climb .brand{left:0;right:0;top:50px;align-items:center}
  .poster-climb .brand-name{font-size:29px}
  .poster-climb .brand-name i{width:18px;height:18px}
  .poster-climb .brand-tag{font-size:11px}
  .climb-sign{position:absolute;left:83px;top:123px;width:176px;height:176px}
  .climb-no{position:absolute;left:0;right:0;top:303px;text-align:center;font-family:"Inter",Arial,sans-serif;font-weight:800;color:var(--orange);font-size:76px;line-height:1;letter-spacing:-.01em}
  .climb-word{position:absolute;left:0;right:0;top:376px;text-align:center;font-weight:600;color:var(--purple);font-size:52px;line-height:1}

  /* Banner */
  .banner{position:absolute;left:50px;top:602px;width:1102px;height:441px;overflow:hidden;background:
      radial-gradient(circle at 2% 45%,#6a8ef7 0 10%,transparent 10.2%),
      radial-gradient(circle at 100% 55%,#6a8ef7 0 12%,transparent 12.2%),
      radial-gradient(circle at 12% 100%,#6a8ef7 0 6%,transparent 6.2%),
      radial-gradient(circle at 88% 100%,#6a9ef7 0 5%,transparent 5.2%),
      radial-gradient(circle at 95% 0%,#5fb0fa 0 10%,transparent 10.2%),
      linear-gradient(90deg,#5ad4fb,#5acbfb 60%,#62b8fa)}
  .banner .card{position:absolute;left:36px;top:24px;width:1030px;height:393px;background:var(--white);border-radius:30px}
  .banner .brand{left:771px;top:56px}
  .banner .brand-name{font-size:40px;gap:8px}
  .banner .brand-name i{width:24px;height:24px}
  .banner .brand-tag{font-size:15px;margin-top:6px}
  .banner-sign{position:absolute;left:89px;top:78px;width:284px;height:284px}
  .banner-no{position:absolute;left:424px;top:150px;font-weight:800;color:var(--green);font-size:128px;line-height:1;letter-spacing:-.01em}
  .banner-word{position:absolute;left:680px;top:184px;font-weight:600;color:var(--yellow);font-size:86px;line-height:1}

  .caption{position:absolute;color:var(--white);font-family:"Inter",Arial,sans-serif;font-weight:300;font-size:18px}
</style>
</head>
<body>
<main class="sheet">

  <!-- A1 Playground rules -->
  <section class="poster poster-rules">
    <span class="pin" style="left:5px;top:46px"></span>
    <div class="card"></div>
    <div class="brand brand-sm" style="left:34px;top:48px">
      <span class="brand-name"><i></i>Tumble Nest</span>
      <span class="brand-tag">MOBILE PLAY CENTRE</span>
    </div>
    <h2 class="age">0-10 year olds ONLY</h2>
    <p class="supervise"><b>Parents/Guardians</b> must supervise children using this play equipment at all times.</p>
    <div class="rules-band">PLAY GROUND<small>Rules</small></div>

    <div class="rule" style="left:34px;top:218px">
      <svg viewBox="0 0 47 47"><circle role="img" aria-label="Shoe icon" cx="23.5" cy="23.5" r="18" fill="#3a3a3a"/><circle cx="23.5" cy="23.5" r="20.5" fill="none" stroke="#e41e26" stroke-width="4"/><line x1="9" y1="9" x2="38" y2="38" stroke="#e41e26" stroke-width="4"/></svg>
      <div><div class="rule-no">No!</div><div class="rule-label">Shoes<small>( Socks must be worn )</small></div></div>
    </div>
    <div class="rule" style="left:178px;top:218px">
      <svg viewBox="0 0 47 47"><circle role="img" aria-label="Child climbing a net icon" cx="23.5" cy="23.5" r="18" fill="#3a3a3a"/><circle cx="23.5" cy="23.5" r="20.5" fill="none" stroke="#e41e26" stroke-width="4"/><line x1="9" y1="9" x2="38" y2="38" stroke="#e41e26" stroke-width="4"/></svg>
      <div><div class="rule-no">No!</div><div class="rule-label">Climbing the<br>Nets</div></div>
    </div>
    <div class="rule" style="left:34px;top:280px">
      <svg viewBox="0 0 47 47"><circle role="img" aria-label="Food and drink icon" cx="23.5" cy="23.5" r="18" fill="#3a3a3a"/><circle cx="23.5" cy="23.5" r="20.5" fill="none" stroke="#e41e26" stroke-width="4"/><line x1="9" y1="9" x2="38" y2="38" stroke="#e41e26" stroke-width="4"/></svg>
      <div><div class="rule-no">No!</div><div class="rule-label">Food or Drink</div></div>
    </div>
    <div class="rule" style="left:178px;top:280px">
      <svg viewBox="0 0 47 47"><circle role="img" aria-label="Bottles and glass icon" cx="23.5" cy="23.5" r="18" fill="#3a3a3a"/><circle cx="23.5" cy="23.5" r="20.5" fill="none" stroke="#e41e26" stroke-width="4"/><line x1="9" y1="9" x2="38" y2="38" stroke="#e41e26" stroke-width="4"/></svg>
      <div><div class="rule-no">No!</div><div class="rule-label">Bottle or Glass</div></div>
    </div>
    <div class="rule" style="left:34px;top:342px">
      <svg viewBox="0 0 47 47"><circle role="img" aria-label="Chewing gum bubble icon" cx="23.5" cy="23.5" r="18" fill="#3a3a3a"/><circle cx="23.5" cy="23.5" r="20.5" fill="none" stroke="#e41e26" stroke-width="4"/><line x1="9" y1="9" x2="38" y2="38" stroke="#e41e26" stroke-width="4"/></svg>
      <div><div class="rule-no">No!</div><div class="rule-label">Chewing Gum</div></div>
    </div>
    <div class="rule" style="left:178px;top:342px">
      <svg viewBox="0 0 47 47"><circle role="img" aria-label="Sharp tools icon" cx="23.5" cy="23.5" r="18" fill="#3a3a3a"/><circle cx="23.5" cy="23.5" r="20.5" fill="none" stroke="#e41e26" stroke-width="4"/><line x1="9" y1="9" x2="38" y2="38" stroke="#e41e26" stroke-width="4"/></svg>
      <div><div class="rule-no">No!</div><div class="rule-label">Sharp Objects</div></div>
    </div>
    <div class="rule" style="left:34px;top:404px">
      <svg viewBox="0 0 47 47"><circle role="img" aria-label="Face paint brushes icon" cx="23.5" cy="23.5" r="18" fill="#3a3a3a"/><circle cx="23.5" cy="23.5" r="20.5" fill="none" stroke="#e41e26" stroke-width="4"/><line x1="9" y1="9" x2="38" y2="38" stroke="#e41e26" stroke-width="4"/></svg>
      <div><div class="rule-no">No!</div><div class="rule-label">Face Painting</div></div>
    </div>
    <div class="rule" style="left:178px;top:404px">
      <svg viewBox="0 0 47 47"><circle role="img" aria-label="Stiletto shoe icon" cx="23.5" cy="23.5" r="18" fill="#3a3a3a"/><circle cx="23.5" cy="23.5" r="20.5" fill="none" stroke="#e41e26" stroke-width="4"/><line x1="9" y1="9" x2="38" y2="38" stroke="#e41e26" stroke-width="4"/></svg>
      <div><div class="rule-no">No!</div><div class="rule-label">Stilettos</div></div>
    </div>
  </section>

  <!-- A1 Toddler zone -->
  <section class="poster poster-toddler">
    <span class="pin" style="left:5px;top:46px"></span>
    <div class="card"></div>
    <div class="brand brand-sm" style="left:36px;top:48px">
      <span class="brand-name"><i></i>Tumble Nest</span>
      <span class="brand-tag">MOBILE PLAY CENTRE</span>
    </div>
    <div class="zone-band">Toddler Zone</div>
    <h2 class="zone-age">0-3 year olds ONLY</h2>
    <p class="zone-notes">Supervision required at all times.<br>• Parents please <em>wear socks</em> too</p>
    <p class="zone-box">If using the toddler soft play equipment, please ensure that this area is used by <em>children 0-3 ONLY</em>. The equipment and ball pit is only designed for small children and bigger kids might injure themselves, the smaller children or <em>cause extensive damage</em> to the equipment, of which there <em>will be a charge</em> back to the client.</p>
  </section>

  <!-- A4 No climbing -->
  <section class="poster poster-climb">
    <span class="pin" style="left:5px;top:46px"></span>
    <div class="card"></div>
    <div class="brand">
      <span class="brand-name"><i></i>Tumble Nest</span>
      <span class="brand-tag">MOBILE PLAY CENTRE</span>
    </div>
    <svg class="climb-sign" viewBox="0 0 176 176">
      <circle role="img" aria-label="Silhouette of a child climbing a net" cx="88" cy="88" r="76" fill="#4a4a4a"/>
      <circle cx="88" cy="88" r="81" fill="none" stroke="#f7891f" stroke-width="14"/>
      <line x1="143" y1="33" x2="33" y2="143" stroke="#f7891f" stroke-width="13"/>
    </svg>
    <div class="climb-no">No!</div>
    <div class="climb-word">Climbing</div>
  </section>

  <p class="caption" style="left:50px;top:539px">A1 Size - Playground rules</p>
  <p class="caption" style="left:429px;top:539px">A1 Size - Toddler Zone</p>
  <p class="caption" style="left:808px;top:539px">A4 Size - No Climbing</p>

  <!-- 20cm x 8cm banner -->
  <section class="banner">
    <span class="pin" style="left:60px;top:430px;width:6px;height:6px;top:428px"></span>
    <div class="card"></div>
    <div class="brand">
      <span class="brand-name"><i></i>Tumble Nest</span>
      <span class="brand-tag">MOBILE PLAY CENTRE</span>
    </div>
    <svg class="banner-sign" viewBox="0 0 284 284">
      <circle role="img" aria-label="Silhouette of a child climbing a net" cx="142" cy="142" r="120" fill="#4a4a4a"/>
      <circle cx="142" cy="142" r="130" fill="none" stroke="#1b75bc" stroke-width="24"/>
      <line x1="230" y1="54" x2="54" y2="230" stroke="#1b75bc" stroke-width="20"/>
    </svg>
    <div class="banner-no">No!</div>
    <div class="banner-word">Climbing</div>
  </section>

  <p class="caption" style="left:50px;top:1060px">20cm x 8cm</p>
</main>
</body>
</html>
```